Bright Hall Meetings: Educators and Families joining forces for pupil growth.

This is a book that helps to prepare for and hold a standard conference that an educator would have with the parents of the students in the school. It is also about how to have problem-solving conferences around difficult issues using techniques from family therapy. Parent involvement is a key ingredient for student success, but most educators have no training in holding meetings with parents. This book fills that gap.
Updates

Need extra days to review

Target Market(s)

Teachers, principals, counselors, school psychologists, school nurses. Anyone who has conferences with the parents of their students.

Font styles to use
Sans Serif

Colors
85acd3
ffcf3e

Requirements
Must have
• I have several books coming up. I'd like something that could be carried over to the new ones without too many changes. They won't all be about education. I am a psychologist so most of my writings will cover subjects related to emotional intelligence.
Nice to have
• Something dignified that will pop out for those in the schools. I like the combination of a royal blue background with white and gold (not yellow) lettering.
Should not have
• I'd like it to be easy to read. Not too messy or too much stuff on the page.

```html
<!DOCTYPE html>
<html lang="en">
<head>
<meta charset="utf-8">
<title>Bright Hall Meetings</title>
<link rel="stylesheet" href="https://fonts.googleapis.com/css2?family=Jost:wght@300;400;600&display=swap">
<style>
  :root {
    --cover-blue: #608db4;
    --gold: #ffcf3e;
    --white: #ffffff;
    --emblem-tone: #c9d9e8;
  }
  html, body {
    margin: 0;
    padding: 0;
    overflow: hidden;
    background: var(--cover-blue);
  }
  .book-cover {
    position: relative;
    width: 933px;
    height: 1200px;
    overflow: hidden;
    background: var(--cover-blue);
    font-family: "Jost", "Century Gothic", sans-serif;
    text-align: center;
  }
  .title {
    position: absolute;
    top: 61px;
    left: 0;
    width: 100%;
    margin: 0;
    color: var(--gold);
    font-weight: 600;
    text-transform: uppercase;
    line-height: 1;
  }
  .title-line-top {
    display: block;
    font-size: 110px;
    letter-spacing: 4px;
  }
  .title-line-main {
    display: block;
    margin-top: -7px;
    font-size: 137px;
    letter-spacing: 5px;
  }
  .tagline-rule {
    position: absolute;
    left: 187px;
    width: 560px;
    height: 2px;
    background: linear-gradient(to right, rgba(255,255,255,0), rgba(255,255,255,0.95) 15%, rgba(255,255,255,0.95) 85%, rgba(255,255,255,0));
  }
  .tagline-rule.top { top: 428px; }
  .tagline-rule.bottom { top: 659px; }
  .tagline {
    position: absolute;
    top: 445px;
    left: 0;
    width: 100%;
    margin: 0;
    color: var(--white);
    font-weight: 300;
    font-size: 41px;
    line-height: 61px;
    letter-spacing: 1px;
  }
  .emblem-area {
    position: absolute;
    left: 336px;
    top: 770px;
    width: 254px;
    height: 244px;
    border-radius: 50%;
    background: radial-gradient(circle at 45% 47%, var(--white) 0%, var(--emblem-tone) 55%, rgba(96,141,180,0) 72%);
  }
  .author {
    position: absolute;
    top: 1120px;
    left: 0;
    width: 100%;
    margin: 0;
    color: var(--gold);
    font-weight: 400;
    font-size: 32px;
  }
</style>
</head>
<body>
  <main class="book-cover">
    <h1 class="title">
      <span class="title-line-top">Bright Hall</span>
      <span class="title-line-main">Meetings</span>
    </h1>

    <div class="tagline-rule top"></div>
    <p class="tagline">Educators and Families<br>joining forces<br>for pupil growth.</p>
    <div class="tagline-rule bottom"></div>

    <div class="emblem-area" role="img" aria-label="Emblem: a white target with a gold arrow in the bullseye"></div>

    <p class="author">Author Name</p>
  </main>
</body>
</html>
```